Boutique Recruiting Firm Needs Eye-Catching Business Cards (and potentially new logo)!

I run a recruiting company in Charleston, South Carolina. I have a ton of networking events coming up and need business cards to grab potential clients attention.

I currently have a logo but if you want to try and recreate the logo to something more modern I am open to that. If you do decide to create a new logo please submit the business card with the old logo and the new one.

Staffing Beyond the Lantern, LLC is the name of my company. I create videos to my clients and candidates which allows me to standout from my competition so I would like a business card (and possibly new logo) to do the same.

I do not specialize in any one industry of recruiting.

Industry/Entity Type

Business

```html
<!DOCTYPE html>
<html lang="en">
<head>
<meta charset="utf-8">
<title>Staffing Beyond the Lantern, LLC — Business Card</title>
<link href="https://fonts.googleapis.com/css2?family=Roboto:wght@400;500;700&display=swap" rel="stylesheet">
<style>
  :root {
    --paper: #ffffff;
    --tan: #d1ae6c;
    --ink: #47474a;
    --ink-soft: #4f4f52;
  }
  * { margin: 0; padding: 0; box-sizing: border-box; }
  html, body { width: 1200px; height: 705px; overflow: hidden; background: var(--paper); }
  .card {
    position: relative;
    width: 1200px;
    height: 705px;
    display: flex;
    font-family: "Roboto", Arial, sans-serif;
    color: var(--ink);
  }
  .brand-side {
    width: 574px;
    height: 100%;
    background: var(--paper);
    display: flex;
    align-items: center;
    justify-content: center;
  }
  .wordmark {
    display: flex;
    align-items: center;
    gap: 22px;
    margin-top: 20px;
  }
  .wordmark-square {
    width: 54px;
    height: 54px;
    background: var(--tan);
    flex: none;
  }
  .wordmark-name {
    font-weight: 700;
    font-size: 44px;
    line-height: 1.1;
    color: var(--ink);
  }
  .info-side {
    flex: 1;
    height: 100%;
    background: var(--tan);
    padding: 98px 0 0 60px;
    position: relative;
  }
  .person-name {
    font-weight: 700;
    font-size: 40px;
    letter-spacing: 0.3px;
    color: var(--ink);
  }
  .person-title {
    margin-top: 12px;
    font-weight: 400;
    font-size: 26px;
    color: var(--ink-soft);
  }
  .contact-list {
    position: absolute;
    left: 58px;
    top: 364px;
    list-style: none;
  }
  .contact-item {
    display: flex;
    align-items: center;
    height: 53px;
    font-size: 27px;
    color: var(--ink);
    letter-spacing: 0.4px;
  }
  .contact-icon {
    width: 34px;
    height: 34px;
    margin-right: 34px;
    flex: none;
  }
  .contact-icon * { fill: none; stroke: var(--ink); stroke-width: 2; }
  .contact-icon .solid { fill: var(--ink); stroke: none; }
</style>
</head>
<body>
<main class="card">
  <section class="brand-side">
    <div class="wordmark">
      <span class="wordmark-square"></span>
      <span class="wordmark-name">Staffing<br>Beyond the<br>Lantern, LLC</span>
    </div>
  </section>

  <section class="info-side">
    <h1 class="person-name">Ravi Deshmukh</h1>
    <p class="person-title">Managing Director</p>

    <ul class="contact-list">
      <li class="contact-item">
        <svg class="contact-icon" viewBox="0 0 34 34" aria-hidden="true">
          <path class="solid" d="M17 2c-6 0-10.5 4.6-10.5 10.3C6.5 20 17 32 17 32s10.5-12 10.5-19.7C27.5 6.6 23 2 17 2zm0 14.5a4.3 4.3 0 1 1 0-8.6 4.3 4.3 0 0 1 0 8.6z"/>
        </svg>
        <span>12 Lake Road, Shanti Vihar</span>
      </li>
      <li class="contact-item">
        <svg class="contact-icon" viewBox="0 0 34 34" aria-hidden="true">
          <circle cx="17" cy="17" r="15"/>
          <path d="M12 9.5l3 3-1.6 2.2c1 2.4 2.6 4 5 5l2.2-1.6 3 3-2 2.2c-5.5-.6-11.2-6.3-11.8-11.8z"/>
        </svg>
        <span>+91 55501 23456</span>
      </li>
      <li class="contact-item">
        <svg class="contact-icon" viewBox="0 0 34 34" aria-hidden="true">
          <rect x="2" y="7" width="30" height="20"/>
          <path d="M2 7l15 12 15-12M2 27l11-10M32 27l-11-10"/>
        </svg>
        <span>hello@beyondlantern.com</span>
      </li>
      <li class="contact-item">
        <svg class="contact-icon" viewBox="0 0 34 34" aria-hidden="true">
          <circle cx="17" cy="17" r="15"/>
          <ellipse cx="17" cy="17" rx="6.5" ry="15"/>
          <path d="M17 2v30M2 17h30M4.5 9.5h25M4.5 24.5h25"/>
        </svg>
        <span>www.staffingbeyondthelantern.com</span>
      </li>
      <li class="contact-item">
        <svg class="contact-icon" viewBox="0 0 34 34" aria-hidden="true">
          <rect class="solid" x="3" y="3" width="28" height="28" rx="4"/>
        </svg>
        <span>social.page/beyondlanternllc</span>
      </li>
    </ul>
  </section>
</main>
</body>
</html>
```